Modern wordpress-enabled design wanted for translations agency serving large corporations

We are a translation agency and we only work for corporate clients and not private individuals. We are currently using the Marrow wordpress theme and an upload feature called quenbox. It is important that prospective clients can upload their file. So we need a cool design for that kind of feature. We offer different kinds of translations tailored to the needs or global corporations. Corporate communications translations, legal translations, financial translations, healthcare translations, financial translations, audit translations.

```html
<!DOCTYPE html>
<html lang="en">
<head>
<meta charset="utf-8">
<title>Corvane Translation</title>
<link href="https://fonts.googleapis.com/css2?family=Raleway:wght@400;500;600;700&family=Open+Sans:wght@400;600&display=swap" rel="stylesheet">
<style>
:root{
  --teal:#1aa3bf;
  --teal-dark:#138aa3;
  --teal-band:#2aa6be;
  --ink:#2d3a44;
  --muted:#8a969e;
  --line:#dfe5e8;
  --white:#ffffff;
  --footer:#222a31;
}
*{margin:0;padding:0;box-sizing:border-box}
html,body{width:1200px;height:2812px;overflow:hidden}
body{background:var(--white);font-family:"Open Sans",sans-serif;color:var(--ink);position:relative}
.abs{position:absolute}

/* header */
.site-header{left:0;top:0;width:1200px;height:112px;background:var(--white);border-bottom:1px solid var(--line)}
.brand{left:100px;top:34px;display:flex;align-items:center;gap:14px}
.brand-dot{width:44px;height:44px;border-radius:50%;background:linear-gradient(135deg,#3fc3dc,var(--teal-dark))}
.brand-name{font-family:"Raleway",sans-serif;font-size:26px;font-weight:500;color:var(--teal)}
.main-nav{right:100px;top:0;display:flex;height:112px}
.main-nav a{display:flex;align-items:flex-end;padding:0 26px 44px;font-family:"Raleway",sans-serif;font-size:15px;color:var(--ink);text-decoration:none}
.main-nav a.active{background:var(--teal);color:var(--white)}

/* hero */
.hero{left:0;top:112px;width:1200px;height:528px;background:radial-gradient(ellipse at 30% 40%,#5d7386 0%,#34495c 35%,#1e2c3a 75%,#16212c 100%)}
.hero-title{left:600px;top:158px;width:560px;text-align:center;white-space:nowrap;font-family:"Raleway",sans-serif;font-weight:600;font-size:32px;line-height:40px;color:var(--white)}
.hero-text{left:640px;top:210px;width:480px;text-align:center;font-size:15px;line-height:22px;color:#e4ecf1}
.hero-btns{left:772px;top:282px;display:flex;gap:32px}
.btn{display:inline-block;padding:10px 18px;font-family:"Raleway",sans-serif;font-size:14px;color:var(--white);border:1px solid var(--white)}
.btn.solid{background:var(--teal);border-color:var(--teal)}
.slider-dots{left:1050px;top:476px;display:flex;gap:10px}
.slider-dots span{width:16px;height:16px;border-radius:50%;border:2px solid #c7d3da}

/* section headings */
.section-title{left:0;width:1200px;text-align:center;font-family:"Raleway",sans-serif;font-weight:500;font-size:30px;line-height:38px;color:var(--teal)}
.section-sub{left:0;width:1200px;text-align:center;font-size:14px;line-height:20px;color:var(--muted)}

/* portfolio */
.portfolio-grid{left:100px;top:772px;width:1000px;height:380px;display:grid;grid-template-columns:repeat(5,1fr);grid-template-rows:188px 188px;gap:4px}
.tile{background:#999}
.tile.feature{background:var(--teal-band);color:var(--white);padding:34px 22px;text-align:center}
.tile.feature h3{font-family:"Raleway",sans-serif;font-size:16px;font-weight:600;margin-bottom:10px}
.tile.feature p{font-size:12px;line-height:18px;margin-bottom:14px}
.tile.feature .more{display:inline-block;font-size:11px;border:1px solid var(--white);padding:4px 12px}
.p1{background:linear-gradient(135deg,#8c7a5e,#d2c2a4)}
.p2{background:linear-gradient(135deg,#cfd7de,#7f9bb0)}
.p3{background:linear-gradient(135deg,#3c4c60,#a8b5c0)}
.p4{background:linear-gradient(135deg,#c9b29b,#5d6f86)}
.p5{background:linear-gradient(135deg,#d8dde2,#6e7e90)}
.p6{background:linear-gradient(135deg,#e2d0ba,#7b8a99)}
.p7{background:linear-gradient(135deg,#b9a48e,#4f6175)}
.p8{background:linear-gradient(135deg,#4a3426,#b18f6d)}
.p9{background:linear-gradient(135deg,#eef2f5,#9ab0c2)}

/* testimonials */
.testimonials{left:0;top:1188px;width:1200px;height:452px;background:linear-gradient(180deg,#34aec6,#1f97b0)}
.testimonials .section-title{color:var(--white);top:56px}
.avatar{left:532px;top:112px;width:136px;height:136px;border-radius:50%;border:5px solid var(--white);background:linear-gradient(135deg,#e3c2a8,#8a5d44)}
.quote-lead{left:0;top:278px;width:1200px;text-align:center;font-size:13px;line-height:18px;color:var(--white);font-weight:600}
.quote-text{left:160px;top:304px;width:880px;text-align:center;font-size:12px;line-height:20px;color:#e9f6f9}
.quote-name{left:0;top:366px;width:1200px;text-align:center;font-size:12px;color:var(--white);line-height:18px}
.quote-mark{font-family:Georgia,serif;font-size:140px;color:rgba(255,255,255,.35);line-height:1}

/* services */
.services-grid{left:100px;top:1824px;width:1000px;display:grid;grid-template-columns:repeat(3,1fr);row-gap:70px}
.service{display:flex;gap:18px;padding-left:50px}
.service-icon{flex:0 0 62px;height:62px;border-radius:50%;border:2px solid var(--teal);display:flex;align-items:center;justify-content:center;color:var(--teal);font-size:28px;font-family:"Raleway",sans-serif}
.service h4{font-family:"Raleway",sans-serif;font-size:14px;font-weight:600;color:var(--ink);margin:4px 0 8px}
.service p{font-size:11px;line-height:17px;color:var(--muted);width:180px}

/* contact */
.contact{left:0;top:2140px;width:1200px;height:440px;background:radial-gradient(ellipse at 40% 80%,#3a4651 0%,#1f2932 55%,#151c22 100%)}
.contact .section-title{color:var(--white);top:54px}
.contact .section-sub{color:#b8c4cc;top:100px}
.field{background:var(--white);border:1px solid #cfd8de;font-size:12px;color:#666;padding:8px 10px}
.upload{left:360px;top:320px;width:580px;height:34px;display:flex;align-items:center;gap:10px;border:1px dashed #8fa1ad;padding:0 6px 0 10px;font-size:12px;color:#c9d3da}
.upload svg{flex:0 0 auto}
.upload .browse{margin-left:auto;background:#3a4651;color:var(--white);font-size:11px;padding:4px 12px}
.submit{left:512px;top:374px;width:176px;height:40px;background:var(--teal);color:var(--white);font-size:13px;text-align:center;line-height:40px}

/* footer */
.footer-band{left:0;top:2580px;width:1200px;height:140px;background:var(--teal)}
.footer-brand{left:0;top:38px;width:1200px;text-align:center;font-family:"Raleway",sans-serif;font-size:30px;font-weight:600;color:var(--white)}
.footer-circles{left:0;top:88px;width:1200px;display:flex;justify-content:center;gap:12px}
.footer-circles span{width:28px;height:28px;border-radius:50%;border:2px solid var(--white)}
.footer-bar{left:0;top:2720px;width:1200px;height:92px;background:var(--footer)}
.footer-nav{left:100px;top:26px;display:flex;gap:44px;font-size:11px;color:#9aa6ae}
.copyright{left:100px;top:56px;font-size:10px;color:#7d8a93}
.footer-dots{right:100px;top:26px;display:flex;gap:8px}
.footer-dots span{width:16px;height:16px;border-radius:50%;border:1px solid #7d8a93}
</style>
</head>
<body>

<header class="site-header abs">
  <div class="brand abs"><span class="brand-dot"></span><span class="brand-name">Corvane Translation</span></div>
  <nav class="main-nav abs">
    <a class="active">Home</a><a>About</a><a>Portfolio</a><a>Services</a><a>Testimonials</a><a>Contact</a>
  </nav>
</header>

<section class="hero abs" role="img" aria-label="Business hand touching a network of connected people figures on a dark blue background">
  <h1 class="hero-title abs">Welcome to Corvane Translation</h1>
  <p class="hero-text abs">Nam liber tempor cum soluta nobis eleifend option congue nihil imperdiet doming id quod mazim placerat facer possim.</p>
  <div class="hero-btns abs"><span class="btn">Learn More</span><span class="btn solid">Get a Quote</span></div>
  <div class="slider-dots abs"><span></span><span></span></div>
</section>

<h2 class="section-title abs" style="top:662px">Portfolio</h2>
<p class="section-sub abs" style="top:712px">Simply dummy text of the printing and typesetting industry. Lorem Ipsum has been the industry's standard dummy text.</p>

<div class="portfolio-grid abs">
  <div class="tile feature">
    <h3>Corporate Translations</h3>
    <p>Accurate documents delivered for global teams across every market.</p>
    <span class="more">Read more</span>
  </div>
  <div class="tile p1" role="img" aria-label="Stacked coins and financial papers"></div>
  <div class="tile p2" role="img" aria-label="Medical team in a hospital"></div>
  <div class="tile p3" role="img" aria-label="Business people in a meeting"></div>
  <div class="tile p4" role="img" aria-label="Businessman at work"></div>
  <div class="tile p5" role="img" aria-label="Business team at a desk"></div>
  <div class="tile p6" role="img" aria-label="Smiling professional"></div>
  <div class="tile p7" role="img" aria-label="Group of colleagues"></div>
  <div class="tile p8" role="img" aria-label="Law books and gavel"></div>
  <div class="tile p9" role="img" aria-label="Doctors in a clinic"></div>
</div>

<section class="testimonials abs">
  <h2 class="section-title abs">Testimonials</h2>
  <div class="avatar abs" role="img" aria-label="Client portrait"></div>
  <span class="quote-mark abs" style="left:60px;top:270px">&#8220;</span>
  <span class="quote-mark abs" style="left:1070px;top:340px">&#8221;</span>
  <p class="quote-lead abs">Nemo enim ipsam voluptatem quia voluptas sit aspernatur aut odit aut fugit, sed quia magni dolores.</p>
  <p class="quote-text abs">Ut fuerat tempor sapiente dolore quis nostrud exercitation ullamco laboris nisi aliquip commodo consequat. Duis aute irure dolor in reprehenderit in voluptate velit esse cillum dolore eu fugiat nulla pariatur excepteur sint occaecat cupidatat non proident sunt in culpa qui officia deserunt.</p>
  <p class="quote-name abs">Jane Halloway<br>CEO, Norvent Group</p>
</section>

<h2 class="section-title abs" style="top:1702px">Our Services</h2>
<p class="section-sub abs" style="top:1752px">Simply dummy text of the printing and typesetting industry. Lorem Ipsum has been the industry's standard dummy text.</p>

<div class="services-grid abs">
  <div class="service">
    <div class="service-icon"><svg width="28" height="24" viewBox="0 0 28 24" fill="none" stroke="currentColor" stroke-width="2"><rect x="2" y="7" width="24" height="15" rx="2"/><path d="M10 7V3h8v4M2 13h24"/></svg></div>
    <div><h4>Corporate com Translations</h4><p>Clear internal and external messages adapted for every audience and region.</p></div>
  </div>
  <div class="service">
    <div class="service-icon"><svg width="28" height="28" viewBox="0 0 28 28" fill="none" stroke="currentColor" stroke-width="2"><path d="M6 12l8-8 4 4-8 8zM12 10l12 12M3 25h12"/></svg></div>
    <div><h4>Legal Translations</h4><p>Contracts, filings and agreements rendered with precise legal terminology.</p></div>
  </div>
  <div class="service">
    <div class="service-icon">$</div>
    <div><h4>Financial Translations</h4><p>Reports, statements and disclosures translated by qualified finance linguists.</p></div>
  </div>
  <div class="service">
    <div class="service-icon"><svg width="28" height="24" viewBox="0 0 28 24" fill="none" stroke="currentColor" stroke-width="2"><rect x="2" y="6" width="24" height="16" rx="2"/><path d="M10 6V2h8v4M14 10v8M10 14h8"/></svg></div>
    <div><h4>Healthcare Translations</h4><p>Clinical, pharmaceutical and patient material handled with medical accuracy.</p></div>
  </div>
  <div class="service">
    <div class="service-icon"><svg width="30" height="20" viewBox="0 0 30 20" fill="none" stroke="currentColor" stroke-width="2"><rect x="2" y="2" width="26" height="16" rx="2"/><circle cx="15" cy="10" r="4"/></svg></div>
    <div><h4>Financial Translations</h4><p>Investor relations, audits and annual reports delivered on tight deadlines.</p></div>
  </div>
  <div class="service">
    <div class="service-icon">$</div>
    <div><h4>Audit Translations</h4><p>Audit findings and compliance files translated for boards and regulators.</p></div>
  </div>
</div>

<section class="contact abs" role="img" aria-label="Dark keyboard close-up background">
  <h2 class="section-title abs">Contact Us</h2>
  <p class="section-sub abs">Simply dummy text of the printing and typesetting industry. Lorem Ipsum has been the industry's standard dummy text.</p>
  <div class="field abs" style="left:360px;top:160px;width:336px;height:34px">Name</div>
  <div class="field abs" style="left:712px;top:160px;width:228px;height:34px">E-mail</div>
  <div class="field abs" style="left:360px;top:204px;width:580px;height:106px">Message*</div>
  <div class="upload abs">
    <svg width="16" height="16" viewBox="0 0 16 16" fill="none" stroke="#c9d3da" stroke-width="1.6"><path d="M8 11V2M4 6l4-4 4 4M2 11v3h12v-3"/></svg>
    <span>Upload your file for a quote</span>
    <span class="browse">Browse</span>
  </div>
  <div class="submit abs">Submit</div>
</section>

<footer>
  <div class="footer-band abs">
    <div class="footer-brand abs">quenbox</div>
    <div class="footer-circles abs"><span></span><span></span><span></span><span></span><span></span></div>
  </div>
  <div class="footer-bar abs">
    <div class="footer-nav abs"><span>Home</span><span>About</span><span>Portfolio</span><span>Services</span><span>Testimonials</span><span>Contact</span></div>
    <p class="copyright abs">© 2015 Corvane Translation. All rights reserved.</p>
    <div class="footer-dots abs"><span></span><span></span><span></span></div>
  </div>
</footer>

</body>
</html>
```